Law Firm Website
Innovative and Professional
Project: Law Firm Website
Law Firm Website - Law
Creative Brief
Law
www.tambelcounsel.com
Please see website.
Please see detailed instructions and images attached.
Modern
deep red as in the brastow site below
left side
http://www.brastow.com/
http://www.tmvg.co.ke/
Please see detailed instructions and suggested images in the attached docs.
vmorkin vmorkin
Comment on #60: At the bottom the phone and fax number should be lined up so the numbers are vertically aligned.
Here are a few more options for the family image: http://www.pixoravault.com/stock-illustration-50291736-family-tree-template.php?st=kq7f3d1 http://www.pixoravault.com/stock-photo-61834207-stone-figures-coastline.php?st=m82c5e0 http://www.pixoravault.com/stock-illustration-73920415-vintage-family-tree-with-golden-pictureholders-and-ribbons-dark-background.php?st=kq7f3d1
P.S. By the visa stamp, I mean the red visa stamp on the top right of the page.
We really like #60. We'd like to switch up one of the images. Specifically, could you switch the hands image with one of a family tree such as: http://www.framelundry.com/pic-82615094/stock-vector-family-tree-kinfolk.html?src=pQwErT7uYhGvBnM-ZxcvbN-5-28 or http://www.corvalimage.com/detail/illustration/portraits-on-family-tree-stock-graphic/38204917 (though I'm not sure green would look good with the existing colors) or a different image that you suggest? Also, can you try some options without the visa stamp on the right. We're not sure about that. Finally, please remove the Quick Contact page. We'd rather have people call or email rather than get in touch that way.
We can't star again, but we also like #31. Three stars.
A few more images: http://www.corvalimage.com/detail/photo/view-of-national-flag-from-harbor-pier-royalty-free-image/259403817 http://www.corvalimage.com/detail/photo/this-is-the-state-dome-during-the-anniversary-of-royalty-free-image/41958302
I do like design #38. For some reason am unable to star. I think the other designs have too many images that compete for attention. #38 is easy on the eyes, a little simpler, so I like that. I also like the white and black header and footing in #8. I know I said red, but that looks very sharp to me.
Please also remove the same-sex category from the home page. This should really be a separate page linked from the family immigration page.
Please see the following links for possible images for the main top image. I'm not liking the look of the green card, social security card and flag. Nor do I really like the airport scene, now that I see it on the page. I am also open to your suggestions on this main images. http://www.pixoravault.com/stock-photo-8351027-immigration.php?st=r4t9b2a http://www.pixoravault.com/stock-photo-27364019-grunge-harbor-monument.php?st=r4t9b2a http://www.pixoravault.com/stock-photo-6152934-grunge-harbor-monument.php?st=r4t9b2a http://www.pixoravault.com/stock-illustration-5930281-harbor-islet.php?st=w6e1k83

```html
<!DOCTYPE html>
<html lang="en">
<head>
<meta charset="utf-8">
<title>The Tambel Law Office — Immigration Law</title>
<link href="https://fonts.googleapis.com/css2?family=Arimo:ital,wght@0,400;0,700;1,700&display=swap" rel="stylesheet">
<style>
:root{
  --red:#9e1b32;
  --red-dark:#7c1226;
  --red-light:#b52a40;
  --gold:#e8b96a;
  --gold-dark:#c9913a;
  --page:#ececec;
  --white:#ffffff;
  --ink:#333333;
  --line:#d6d6d6;
}
*{margin:0;padding:0;box-sizing:border-box}
html,body{width:1200px;height:1099px;overflow:hidden}
body{font-family:"Arimo",Arial,sans-serif;background:var(--page);color:var(--ink);position:relative}

.site-header{position:absolute;left:0;top:0;width:1200px;height:140px;background:linear-gradient(var(--red-light),var(--red) 60%,var(--red-dark))}
.brand{position:absolute;left:150px;top:14px;display:flex;align-items:center;gap:12px}
.brand-mark{width:22px;height:22px;border-radius:50%;border:3px solid var(--gold)}
.brand-name{font-size:22px;font-weight:700;color:var(--gold)}
.call-tab{position:absolute;right:140px;top:0;height:36px;padding:0 22px 0 18px;background:linear-gradient(var(--gold),var(--gold-dark));border-radius:0 0 8px 8px;display:flex;align-items:center;gap:10px;font-size:19px;color:var(--white)}
.call-tab strong{font-weight:700}
.main-nav{position:absolute;left:486px;top:64px;display:flex;gap:10px}
.main-nav a{font-size:15px;color:var(--white);text-decoration:none;padding:7px 16px;border-radius:3px}
.main-nav a.current{background:linear-gradient(var(--gold),var(--gold-dark))}

.hero{position:absolute;left:144px;top:156px;width:918px;height:378px;background:var(--white);padding:10px;box-shadow:0 4px 10px rgba(0,0,0,.25)}
.hero-photo{position:relative;width:100%;height:100%;background:linear-gradient(180deg,#d9d2e6 0%,#b3a9c9 45%,#6e6688 75%,#3b3650 100%)}
.hero-caption{position:absolute;right:14px;bottom:44px;width:660px;font-size:16px;font-weight:700;font-style:italic;color:var(--white);line-height:1.35;text-align:right;text-shadow:0 1px 3px rgba(0,0,0,.6)}
.hero-dots{position:absolute;right:18px;bottom:14px;display:flex;gap:6px}
.hero-dots span{width:10px;height:10px;border-radius:50%;background:#bbb}
.hero-dots span.on{background:var(--gold)}

.practice-cards{position:absolute;left:141px;top:615px;width:933px;display:flex;justify-content:space-between}
.card{width:213px;height:279px;background:var(--white);border:1px solid var(--line);border-radius:10px;box-shadow:0 2px 6px rgba(0,0,0,.15);padding:0 8px;text-align:center}
.card-title{margin:0 4px;height:38px;padding:2px 6px;background:var(--red);border-radius:0 0 8px 8px;color:var(--white);font-size:14px;font-weight:700;display:flex;align-items:center;justify-content:center;line-height:1.1}
.card-image{height:146px;margin-top:8px;border:1px solid var(--line)}
.img-family{background:linear-gradient(135deg,#c98a5a,#8a6048 50%,#d9b08a)}
.img-business{background:linear-gradient(160deg,#f2f2f2,#9a9a9a)}
.img-reform{background:linear-gradient(160deg,#e9e3d6,#c98a8a 60%,#a0a0a0)}
.img-couples{background:linear-gradient(160deg,#e6dfe2,#b9b0bf)}
.card-text{margin-top:10px;font-size:12px;line-height:1.45;color:#444}

.site-footer{position:absolute;left:0;top:936px;width:1200px;height:163px;background:var(--red);color:var(--white);text-align:center}
.footer-nav{margin-top:14px;font-size:13px}
.footer-nav a{color:var(--white);text-decoration:none;margin:0 4px}
.footer-line{margin-top:8px;font-size:12px}
.disclaimer{width:830px;margin:6px auto 0;font-size:10.5px;line-height:1.45;opacity:.9}
.payment{margin-top:12px;font-size:12px;display:flex;justify-content:center;align-items:center;gap:10px}
.payment b{font-weight:700}
.pay-icon{width:22px;height:16px;border:2px solid var(--white);border-radius:2px}
</style>
</head>
<body>

<header class="site-header">
  <div class="brand"><span class="brand-mark"></span><span class="brand-name">The Tambel Law Office</span></div>
  <div class="call-tab">
    <svg width="18" height="18" viewBox="0 0 24 24" fill="#fff"><path d="M6.6 10.8a15.1 15.1 0 0 0 6.6 6.6l2.2-2.2a1 1 0 0 1 1-.25 11.4 11.4 0 0 0 3.6.57 1 1 0 0 1 1 1V20a1 1 0 0 1-1 1A17 17 0 0 1 3 4a1 1 0 0 1 1-1h3.5a1 1 0 0 1 1 1c0 1.250.2 2.45.57 3.57a1 1 0 0 1-.25 1z"/></svg>
    <span>Call Us Today</span><strong>312-555-0193</strong>
  </div>
  <nav class="main-nav">
    <a class="current" href="#">Home</a><a href="#">About</a><a href="#">Practice Areas</a><a href="#">Immigration News</a><a href="#">Contact us</a>
  </nav>
</header>

<section class="hero">
  <div class="hero-photo" role="img" aria-label="Travellers silhouetted against a large airport window">
    <p class="hero-caption">The Tambel Law Office is an experienced U.S. immigration firm dedicated to serving individuals and businesses through the practice of immigration law.</p>
    <div class="hero-dots"><span class="on"></span><span></span><span></span></div>
  </div>
</section>

<section class="practice-cards">
  <article class="card">
    <h2 class="card-title">Family Immigration Law</h2>
    <div class="card-image img-family" role="img" aria-label="Stacked hands of a family"></div>
    <p class="card-text">Green Cards, Immediate Relative Petitions, Spouse Visas, Fiancé Visas, Naturalization &amp; Citizenship, Hardship Waivers</p>
  </article>
  <article class="card">
    <h2 class="card-title">Business Immigration Law</h2>
    <div class="card-image img-business" role="img" aria-label="Drawing of a businessman at a desk"></div>
    <p class="card-text">H-1Bs, L-1s, PERM Labor Certifications, Employment-Based Green Cards, Investor &amp; Treaty Trader Visas</p>
  </article>
  <article class="card">
    <h2 class="card-title">Comprehensive Immigration Reform 2014</h2>
    <div class="card-image img-reform" role="img" aria-label="Notice board with a large question mark"></div>
    <p class="card-text">Click Here for the Latest on Immigration Reform 2014!</p>
  </article>
  <article class="card">
    <h2 class="card-title">Same-Sex Couple Immigration</h2>
    <div class="card-image img-couples" role="img" aria-label="Photo of a waving flag"></div>
    <p class="card-text">We Help Same-Sex Couples Navigate Recent Changes in Immigration Law</p>
  </article>
</section>

<footer class="site-footer">
  <nav class="footer-nav"><a href="#">Home</a>| <a href="#">About</a>| <a href="#">Practice Areas</a>| <a href="#">Immigration News</a>| <a href="#">Contact us</a></nav>
  <p class="footer-line">Tambel Law Office. All Rights Reserved | 418 West Harlan Street, 3rd Floor, Chicago, IL 60610 | 312-555-0193</p>
  <p class="disclaimer">The information on this website is for general information purposes only. Nothing on this or associated pages, documents, comments, answers, emails, or other communications should be taken as legal advice for any individual case or situation. This information on this website is not intended to create, and receipt or viewing of this information does not constitute, an attorney-client relationship.</p>
  <div class="payment"><span>We accept the following payment methods:</span><b>Cash</b><span class="pay-icon"></span><b>Check</b><span class="pay-icon"></span></div>
</footer>

</body>
</html>
```